Design profile for MuroDeck Nordhaven

I had a logo competition here recently, and was left with two logos that I could not choose between. Therefore, I create this competition where I want a complete design package or a visual identity for the company. I want you to create design elements that can be used both in print and online. (letterhead, envelopes, business card, website, facebook, etc.) I have also attached a picture of the car I have ordered. I'm happy if you can show how the design can be used on that as well.
What is important is that the logos are treated individually, and that the design you create reflects or builds up under the logo. I want the design to be recognizable and to have a connection with the logo and what we do. (take fizzo lumo as an example. if you remove the name, but keep the red color and the white line, then you will recognize which brand it is about right away)
You choose whether you want to make proposals only for one logo, or or both, but it is important that they are treated individually. The best overall package determines which logo I use.
I have also added an image that you can use as an example background if you want it in a facebook banner for example.
It is important that the design looks professional and unique. A number of designs have come in, but many of the designs are very similar and general. Here is a video of the printer if you need inspiration: https://clipvault.example/v/Q8ZtrMx2LwK

Industry/Entity Type

WallPrinting

Requirements
Must have
• Unique an professional design that can be used both online and print
Nice to have
• Show how to use the design on a VX Tully. (see photos attached)
Should not have
• The design can be simple, but not too simple and general. I want it to give the company an identity

```html
<!DOCTYPE html>
<html lang="en">
<head>
<meta charset="utf-8">
<title>MuroDeck Nordhaven – Business Card</title>
<link rel="stylesheet" href="https://fonts.googleapis.com/css2?family=Roboto+Condensed:ital,wght@0,400;0,700;1,700&display=swap">
<style>
  :root {
    --backdrop: #f1f1f1;
    --card-white: #ffffff;
    --ink: #0a0a0c;
    --paper-text: #ffffff;
    --brand-red: #e30613;
    --brand-yellow: #ffd200;
    --brand-sky: #2fb4e9;
    --stripe-sky: #3aa9e0;
    --font-main: "Roboto Condensed", "Arial Narrow", sans-serif;
  }
  * { box-sizing: border-box; margin: 0; padding: 0; }
  html, body {
    width: 1200px;
    height: 857px;
    overflow: hidden;
    background: var(--backdrop);
    font-family: var(--font-main);
  }
  .canvas { position: relative; width: 1200px; height: 857px; }

  .card {
    position: absolute;
    left: 346px;
    width: 508px;
    height: 291px;
    overflow: hidden;
  }

  /* Front */
  .card--front {
    top: 102px;
    background: var(--card-white);
    border: 1px solid var(--ink);
  }
  .front__brand {
    position: absolute;
    left: 62px;
    top: 58px;
    font-size: 25px;
    font-weight: 700;
    color: var(--ink);
    letter-spacing: 0.2px;
    white-space: nowrap;
  }
  .front__person {
    position: absolute;
    left: 62px;
    top: 126px;
    font-size: 19px;
    font-weight: 700;
    line-height: 1;
    white-space: nowrap;
  }
  .front__first { color: var(--brand-red); }
  .front__last { color: var(--brand-sky); }
  .front__title {
    position: absolute;
    left: 62px;
    top: 152px;
    font-size: 14px;
    font-weight: 700;
    font-style: italic;
    color: var(--ink);
    letter-spacing: 0.3px;
  }
  .front__web {
    position: absolute;
    right: 45px;
    top: 152px;
    font-size: 15px;
    font-weight: 700;
    color: var(--ink);
  }
  .stripe { position: absolute; left: 0; width: 100%; }
  .stripe--sky { top: 199px; height: 3px; background: var(--stripe-sky); }
  .stripe--yellow { top: 202px; height: 6px; background: var(--brand-yellow); }
  .stripe--red { top: 207px; height: 10px; background: var(--brand-red); }

  .front__footer {
    position: absolute;
    left: 0;
    top: 217px;
    width: 100%;
    height: 74px;
    background: var(--ink);
    color: var(--paper-text);
  }
  .contact {
    position: absolute;
    font-size: 14.5px;
    line-height: 22px;
    white-space: nowrap;
  }
  .contact--address { left: 93px; top: 14px; }
  .contact--reach { left: 298px; top: 14px; }
  .icon { position: absolute; }
  .icon--pin { left: 64px; top: 18px; }
  .icon--phone { left: 272px; top: 15px; }
  .icon--mail { left: 271px; top: 40px; }
  .footer__divider {
    position: absolute;
    left: 230px;
    top: 19px;
    width: 1px;
    height: 32px;
    background: var(--paper-text);
  }

  /* Back */
  .card--back {
    top: 464px;
    height: 290px;
    background: var(--ink);
    display: flex;
    align-items: center;
    justify-content: center;
  }
  .back__brand {
    font-size: 44px;
    font-weight: 700;
    color: var(--paper-text);
    letter-spacing: 0.5px;
    white-space: nowrap;
  }
</style>
</head>
<body>
<main class="canvas">

  <section class="card card--front" aria-label="Business card front">
    <div class="front__brand">MuroDeck Nordhaven</div>

    <p class="front__person"><span class="front__first">First Name</span> <span class="front__last">Last Name</span></p>
    <p class="front__title">TITTLE</p>
    <p class="front__web">WWW.WEBSITE.COM</p>

    <div class="stripe stripe--sky"></div>
    <div class="stripe stripe--yellow"></div>
    <div class="stripe stripe--red"></div>

    <div class="front__footer">
      <svg class="icon icon--pin" width="24" height="32" viewBox="0 0 24 32" aria-hidden="true">
        <path d="M12 2C6.8 2 2.8 6 2.8 11.1c0 6.6 9.2 18.4 9.2 18.4s9.2-11.8 9.2-18.4C21.2 6 17.2 2 12 2z" fill="none" stroke="#fff" stroke-width="2"/>
        <circle cx="12" cy="11.2" r="3.6" fill="none" stroke="#fff" stroke-width="2"/>
      </svg>
      <p class="contact contact--address">1234 Streetname<br>City, State 123456</p>

      <div class="footer__divider"></div>

      <svg class="icon icon--phone" width="22" height="20" viewBox="0 0 22 20" aria-hidden="true">
        <path d="M4 2.5l3 3.2-1.6 2c1.2 2.5 3 4.4 5.6 5.6l2-1.6 3.2 3-1.8 2.6C8.6 16.6 3.4 11.4 1.6 4.5z" fill="#fff"/>
        <path d="M12 3.5a5 5 0 0 1 5 5M12 0.8a7.8 7.8 0 0 1 7.8 7.8" fill="none" stroke="#fff" stroke-width="1.3"/>
      </svg>
      <svg class="icon icon--mail" width="24" height="16" viewBox="0 0 24 16" aria-hidden="true">
        <rect x="1" y="1" width="22" height="14" fill="none" stroke="#fff" stroke-width="1.5"/>
        <path d="M1 1l11 8 11-8M1 15l8-7M23 15l-8-7" fill="none" stroke="#fff" stroke-width="1.3"/>
      </svg>
      <p class="contact contact--reach">123-456-7890<br>firstname@website.com</p>
    </div>
  </section>

  <section class="card card--back" aria-label="Business card back">
    <div class="back__brand">MuroDeck Nordhaven</div>
  </section>

</main>
</body>
</html>
```